Design a Word Template and Powerpoint Template for a Venture Capital Fund

I'm looking to get a powerpoint template and word template designed ASAP under the same selected design. Its for a finance / Venture Capital business... keen to keep it clean but "pop" and stand up on its own as a strong brand, solid templates etc... Happy to talk. Thanks Kit

Target Market(s)

Venture Capital and Private Equity

Industry/Entity Type

Finance / Venture Capital / Management Consulting

Requirements
Nice to have
• Strong formatting, icons and optionality, images can be good too

```html
<!DOCTYPE html>
<html lang="en">
<head>
<meta charset="utf-8">
<title>Northgate Ventures Letterhead</title>
<link rel="stylesheet" href="https://fonts.googleapis.com/css2?family=Roboto:wght@300;400&family=Great+Vibes&display=swap">
<style>
  :root {
    --backdrop: #e3e3e3;
    --paper: #f1f1f1;
    --ink: #2a2a2a;
    --ink-soft: #555555;
    --band: #2c2c2e;
    --band-text: #e8e8e8;
    --rule: #8a8a8a;
  }
  * { margin: 0; padding: 0; box-sizing: border-box; }
  html, body {
    width: 1200px;
    height: 1200px;
    overflow: hidden;
    background: var(--backdrop);
    font-family: "Roboto", Arial, sans-serif;
    font-weight: 300;
    color: var(--ink);
  }
  .letterhead {
    position: absolute;
    left: 197px;
    top: 30px;
    width: 806px;
    height: 1140px;
    background: var(--paper);
    box-shadow: 0 6px 22px rgba(0, 0, 0, 0.12);
  }
  .brand {
    position: absolute;
    top: 70px;
    left: 0;
    width: 100%;
    display: flex;
    justify-content: center;
    align-items: center;
    gap: 12px;
  }
  .brand-square {
    width: 14px;
    height: 14px;
    background: var(--ink);
  }
  .brand-name {
    font-size: 20px;
    font-weight: 300;
    letter-spacing: 4px;
    color: var(--ink);
  }
  .letter-text {
    position: absolute;
    left: 86px;
    width: 634px;
    font-size: 13.4px;
    line-height: 19px;
  }
  .date { top: 269px; }
  .recipient { top: 307px; }
  .salutation { top: 401px; }
  .body-para { text-align: justify; }
  .para-1 { top: 439px; }
  .para-2 { top: 591px; }
  .para-3 { top: 705px; }
  .closing { top: 856px; }
  .signature {
    position: absolute;
    left: 90px;
    top: 876px;
    font-family: "Great Vibes", cursive;
    font-size: 27px;
    color: var(--ink);
  }
  .footer-rule {
    position: absolute;
    top: 1057px;
    left: 377px;
    width: 52px;
    height: 1px;
    background: var(--rule);
  }
  .contact-line {
    position: absolute;
    top: 1073px;
    left: 0;
    width: 100%;
    display: flex;
    justify-content: center;
    gap: 12px;
    font-size: 13px;
    color: var(--ink-soft);
  }
  .contact-item { display: flex; align-items: center; gap: 5px; }
  .contact-item svg { width: 10px; height: 10px; }
  .address-band {
    position: absolute;
    left: 0;
    bottom: 0;
    width: 100%;
    height: 30px;
    background: var(--band);
    color: var(--band-text);
    font-size: 13px;
    display: flex;
    align-items: center;
    justify-content: center;
  }
</style>
</head>
<body>
  <main class="letterhead">
    <header class="brand">
      <span class="brand-square"></span>
      <span class="brand-name">NORTHGATE VENTURES</span>
    </header>

    <p class="letter-text date">01 January 2050</p>
    <p class="letter-text recipient">Company (Pvt) Ltd.<br>PO Box 3355 Mainville St<br>Sample City Country 3355</p>
    <p class="letter-text salutation">Dear Daniel Hartley,</p>

    <p class="letter-text body-para para-1">Lorem ipsum dolor sit amet, consectetuer adipiscing elit, sed diam nonummy nibh euismod tincidunt ut laoreet dolore magna aliquam erat volutpat. Ut wisi enim ad minim veniam, quis nostrud exerci tation ullamcorper suscipit lobortis nisl ut aliquip ex ea commodo consequat. Duis dolore te feugait nulla facilisi. Nam liber tempor cum soluta nobis eleifend option congue nihil imperdiet doming id quod mazim placerat facer possim assum. Lorem ipsum dolor sit amet, consectetuer adipiscing elit, sed diam nonummy nibh euismod tincidunt ut laoreet dolore magna aliquam erat volutpat. Ut wisi enim ad minim veniam, quis nostrud exerci tation ullamcorper suscipit lobortis nisl ut aliquip ex ea commodo consequat.</p>

    <p class="letter-text body-para para-2">Consectetuer adipiscing elit, sed diam nonummy nibh euismod tincidunt ut laoreet dolore magna aliquam erat volutpat. Ut wisi enim ad minim veniam, quis nostrud exerci tation ullamcorper suscipit lobortis nisl ut aliquip ex ea commodo consequat. Consectetuer adipiscing elit, sed diam nonummy nibh euismod tincidunt ut laoreet dolore magna aliquam erat volutpat. Ut wisi enim ad minim veniam, quis nostrud exerci tation ullamcorper suscipit lobortis nisl ut aliquip ex ea commodo consequat.</p>

    <p class="letter-text body-para para-3">Consectetuer adipiscing elit, sed diam nonummy nibh euismod tincidunt ut laoreet dolore magna aliquam erat volutpat. Ut wisi enim ad minim veniam, quis nostrud exerci tation ullamcorper suscipit lobortis nisl ut aliquip ex ea commodo consequat. Consectetuer adipiscing elit, sed diam nonummy nibh euismod tincidunt ut laoreet dolore magna aliquam erat volutpat. Ut wisi enim ad minim veniam, quis nostrud exerci tation ullamcorper suscipit lobortis nisl ut aliquip ex ea commodo consequat.</p>

    <p class="letter-text closing">Sincerely Yours</p>
    <p class="signature">Kit Hollis</p>

    <div class="footer-rule"></div>
    <div class="contact-line">
      <span class="contact-item">
        <svg viewBox="0 0 10 10" aria-hidden="true"><path d="M2 0.8 L3.6 0.8 L4.2 3 L3 3.8 Q4 6 6.2 7 L7 5.8 L9.2 6.4 L9.2 8 Q9 9.4 7.6 9.2 Q1.2 8.4 0.8 2.4 Q0.7 0.9 2 0.8 Z" fill="#555"/></svg>
        +61 400-555-214
      </span>
      <span class="contact-item">
        <svg viewBox="0 0 10 10" aria-hidden="true"><rect x="0.5" y="2" width="9" height="6.5" fill="#555"/><path d="M0.8 2.3 L5 5.6 L9.2 2.3" stroke="#f1f1f1" stroke-width="0.9" fill="none"/></svg>
        kit@kithollis.com
      </span>
      <span class="contact-item">
        <svg viewBox="0 0 10 10" aria-hidden="true"><g fill="none" stroke="#555" stroke-width="0.9"><circle cx="5" cy="5" r="4.3"/><ellipse cx="5" cy="5" rx="1.8" ry="4.3"/><line x1="0.7" y1="5" x2="9.3" y2="5"/></g></svg>
        www.northgatevc.com.au
      </span>
    </div>
    <footer class="address-band">Co.Street, Park Ave, Building, Suite, City/State, Zip Code</footer>
  </main>
</body>
</html>
```